Window Cleaning Flyer targeting body corporates

Need a flyer for window cleaning targeting body corporate (approx A5 print size). It should be professional and match the logo attached.
We are looking to standout but not be to over the top for a window cleaning/services company.
We want to entice the receptionist or managers to call us because they see no good reason not to.

Industry/Entity Type

Window Cleaning

Font styles to use
Serif

Colors
0555a3
fbed22

Requirements
Must have
• Professional with a few of the photos attached included. Must include logo and the following contact details:
• Ph: 9413 6570
• email: admin@brightpaneworks.com.au
• PO Box 4726
• Marlowe Heights
• 3284
Nice to have
• Colours matching logo/ van print layout. Looking for more of a simplistic professional design.
Should not have
• Cartoon pictures, animated decorations or stock photos.

```html
<!DOCTYPE html>
<html lang="en">
<head>
<meta charset="utf-8">
<title>Brightpane Window Cleaning – Body Corporate Flyer</title>
<link href="https://fonts.googleapis.com/css2?family=Oswald:wght@700&family=Fira+Sans:wght@500;600&family=Open+Sans:wght@400;700&display=swap" rel="stylesheet">
<style>
  :root {
    --brand-blue: #0555a3;
    --deep-blue: #0b4f86;
    --brand-yellow: #fbed22;
    --box-yellow: #f8d90f;
    --text-dark: #3a3a3a;
    --band-grey: rgba(110, 110, 115, 0.75);
    --paper: #ffffff;
  }
  * { box-sizing: border-box; margin: 0; padding: 0; }
  html, body { width: 932px; height: 1200px; overflow: hidden; background: var(--paper); }
  .flyer { position: relative; width: 932px; height: 1200px; background: var(--paper); font-family: "Fira Sans", sans-serif; }

  .hero-photo {
    position: absolute; left: 0; top: 0; width: 932px; height: 538px;
    background: linear-gradient(135deg, #3d4c5c 0%, #6f8aa3 35%, #9dbad6 60%, #5d7a5a 85%, #c9ccd0 100%);
  }
  .call-band {
    position: absolute; left: 0; top: 457px; width: 525px; height: 81px;
    background: var(--band-grey);
    display: flex; align-items: center; padding-left: 92px;
  }
  .call-band span {
    font-family: "Oswald", sans-serif; font-weight: 700; font-size: 50px;
    color: var(--brand-yellow); letter-spacing: 1px;
  }
  .brand-box {
    position: absolute; left: 525px; top: 391px; width: 345px; height: 147px;
    background: var(--deep-blue); border-radius: 6px 6px 0 0;
    display: flex; flex-direction: column; justify-content: center; align-items: center;
    color: var(--brand-yellow); font-family: "Fira Sans", sans-serif; font-weight: 600;
  }
  .brand-box .name { font-size: 46px; line-height: 1; letter-spacing: 1px; }
  .brand-box .trade { font-size: 22px; letter-spacing: 1.5px; margin-top: 10px; }

  .contact-strip {
    position: absolute; left: 0; top: 538px; width: 932px; height: 34px;
    background: var(--brand-yellow);
    display: flex; align-items: center; justify-content: space-between;
    padding: 0 62px 0 94px;
    font-family: "Open Sans", sans-serif; font-weight: 700; font-size: 16.5px; color: #1a1a1a;
  }

  .headline {
    position: absolute; left: 0; top: 604px; width: 932px; text-align: center;
    font-family: "Oswald", sans-serif; font-weight: 700; font-size: 52px; line-height: 58px;
    color: var(--deep-blue); letter-spacing: 0.5px;
  }
  .intro {
    position: absolute; left: 0; top: 736px; width: 932px; text-align: center;
    font-family: "Open Sans", sans-serif; font-size: 19.5px; line-height: 30px; color: var(--text-dark);
  }

  .pride-note {
    position: absolute; left: 41px; top: 837px; width: 295px; height: 297px;
    background: linear-gradient(180deg, var(--box-yellow), var(--brand-yellow));
    box-shadow: 0 2px 6px rgba(0,0,0,0.25);
    display: flex; align-items: center; justify-content: center; text-align: center;
    font-weight: 600; font-size: 25px; line-height: 41px; color: #1f1f1f; padding: 0 14px;
  }

  .services { position: absolute; left: 383px; top: 822px; width: 520px; color: var(--text-dark); }
  .services h2 { font-weight: 600; font-size: 25px; color: var(--deep-blue); margin-bottom: 14px; }
  .services ul { list-style: none; }
  .services li { position: relative; padding-left: 36px; font-weight: 500; font-size: 22.5px; line-height: 30px; margin-bottom: 12px; }
  .services li::before {
    content: ""; position: absolute; left: 2px; top: 7px; width: 17px; height: 17px;
    border-radius: 50%; background: var(--deep-blue); box-shadow: 0 1px 2px rgba(0,0,0,0.35);
  }
  .services li.lead { font-size: 30px; line-height: 34px; font-weight: 500; letter-spacing: 0.5px; }

  .footer-band { position: absolute; left: 0; top: 1114px; width: 932px; height: 86px; }
  .footer-text {
    position: absolute; left: 0; top: 1140px; width: 932px; text-align: center;
    font-weight: 600; font-size: 28px; color: var(--brand-yellow);
  }
</style>
</head>
<body>
<main class="flyer">
  <div class="hero-photo" role="img" aria-label="Photo of two uniformed window cleaners using extension poles on a car showroom's glass frontage"></div>
  <div class="call-band"><span>Call 9413 6570</span></div>
  <div class="brand-box">
    <span class="name">BRIGHTPANE</span>
    <span class="trade">WINDOW CLEANING</span>
  </div>
  <div class="contact-strip">
    <span>email: admin@brightpaneworks.com.au</span>
    <span>PO Box 4726, Marlowe Heights, 3284</span>
  </div>

  <h1 class="headline">LET BRIGHTPANE TAKE CARE OF YOUR<br>BODY CORPORATE NEEDS!</h1>
  <p class="intro">With over 15 years of experience we will ensure the job is<br>completed to the highest standard everytime..</p>

  <svg class="footer-band" viewBox="0 0 932 86" width="932" height="86" aria-hidden="true">
    <polygon points="0,0 392,0 413,22 932,22 932,86 0,86" fill="#0b4f86"/>
  </svg>

  <p class="pride-note">Most importantly, Brightpane Window Cleaning take pride in being friendly and courteous to all residents.</p>

  <section class="services">
    <h2>Brightpane Specialises In Body Corporate:</h2>
    <ul>
      <li class="lead">WINDOW CLEANING</li>
      <li>Gutter Cleaning (using our ladder free gutter vacuum)</li>
      <li>Pressure Washing including moss treatment to prevent mould regrowth on concrete surface</li>
    </ul>
  </section>

  <p class="footer-text">Contact the Brightpane Team for an easy, FREE quote today!</p>
</main>
</body>
</html>
```